'Orla Property Development' Business Card

Business Card Features:

High Quality (potentially textured) thick card - preference is white textured card

Logo (supplied)

We plan to use the vertical logo as the main logo. But i am happy for people to use either if they find it works better for the design of the card.

The building icon and also the insert to the 'E' is in a metallic finish, i think this should be finished in a metallic embossed or raised style.
Updates

Please note i have attached both a horizontal and Vertical Logo for your reference. We plan to use the vertical logo as the main logo. But i am happy for people to use either if they find it works better for the design of the card.

Please note i am considering having the cards made on stainless steel. This introduces the option of having cut outs in the card and etching or printing for the design. If you have a good concept for this please submit.

http://www.quorvantprint.co.uk/black-metal-cards# this is a site that makes the metal cards to offer some direction . . . . Please note i am basic the selection o the best design, if that means normal print cards on paper then this is what i will choose. But there are some great options with the metal. Thanks.

Industry/Entity Type

Building

Requirements
Must have
• Helvetica font to details side of card - logo as supplied to opposite side.

Card Details:

Darren Ashcombe
Managing Director

+61 438 615 207
+61 3 8276 4139

PO Box 73
Bentleigh, VIC 3024

darren@orla.properties

www.orla.properties

```html
<!DOCTYPE html>
<html lang="en">
<head>
<meta charset="utf-8">
<title>Orla Property Development – Business Card</title>
<link href="https://fonts.googleapis.com/css2?family=Lato:wght@400;700;900&display=swap" rel="stylesheet">
<style>
  :root {
    --canvas: #d9d9d9;
    --card-black: #050505;
    --card-glow: #262626;
    --panel: #2d2d2d;
    --band: #c4c4c4;
    --text-light: #a6a6a6;
    --text-name: #8f8f8f;
    --brand: #8a8a8a;
    --chip-dark: #4d5556;
    --chip-mid: #7c8485;
    --chip-light: #b7b7b7;
  }
  * { margin: 0; padding: 0; box-sizing: border-box; }
  html, body {
    width: 1200px; height: 926px; overflow: hidden;
    background: var(--canvas);
    font-family: "Lato", Helvetica, Arial, sans-serif;
  }
  .sheet {
    width: 1200px; height: 926px;
    display: flex; flex-direction: column;
    align-items: center; justify-content: center; gap: 40px;
  }
  .card {
    position: relative;
    width: 680px; height: 416px;
    overflow: hidden;
    box-shadow: 0 8px 24px rgba(0,0,0,.25);
  }
  /* Front */
  .card--front {
    background: radial-gradient(ellipse at 50% 55%, var(--card-glow) 0%, var(--card-black) 60%);
    display: flex; align-items: center; justify-content: center;
  }
  .brand {
    display: flex; align-items: center; gap: 14px;
    color: var(--brand); font-weight: 700;
    text-transform: uppercase; letter-spacing: 2px;
  }
  .brand__mark { width: 22px; height: 22px; background: var(--brand); flex: none; }
  .card--front .brand { font-size: 26px; }
  /* Back */
  .card--back { background: var(--card-black); }
  .card__art { position: absolute; inset: 0; }
  .card--back .brand {
    position: absolute; left: 36px; top: 158px;
    width: 220px;
    font-size: 17px; line-height: 24px; gap: 10px; letter-spacing: 1.5px;
  }
  .card--back .brand__mark { width: 16px; height: 16px; }
  .details { position: absolute; left: 372px; top: 74px; color: var(--text-light); }
  .details__name {
    font-size: 26px; font-weight: 700; color: var(--text-name);
    text-transform: uppercase; letter-spacing: 1px; white-space: nowrap;
  }
  .details__role { font-size: 17px; font-weight: 700; color: var(--text-name); margin-top: 2px; }
  .contact { list-style: none; margin-top: 30px; }
  .contact__item {
    display: flex; align-items: flex-start; gap: 14px;
    font-size: 20px; line-height: 24px; margin-bottom: 9px;
  }
  .contact__icon { width: 18px; height: 18px; flex: none; margin-top: 3px; fill: var(--text-light); }
</style>
</head>
<body>
<main class="sheet">

  <section class="card card--front" aria-label="Card front">
    <div class="brand"><span class="brand__mark"></span>Orla Property Development</div>
  </section>

  <section class="card card--back" aria-label="Card back">
    <svg class="card__art" viewBox="0 0 680 416" aria-hidden="true">
      <path d="M296 0 Q318 250 194 416 L680 416 L680 0 Z" fill="var(--band)"/>
      <path d="M310 0 Q332 250 212 416 L680 416 L680 0 Z" fill="var(--panel)"/>
      <rect x="0" y="120" width="12" height="26" fill="var(--chip-mid)"/>
      <rect x="0" y="156" width="12" height="26" fill="var(--chip-light)"/>
      <rect x="0" y="192" width="12" height="26" fill="var(--chip-dark)"/>
    </svg>

    <div class="brand"><span class="brand__mark"></span><span>Orla Property Development</span></div>

    <div class="details">
      <h1 class="details__name">Darren Ashcombe</h1>
      <p class="details__role">Managing Director</p>
      <ul class="contact">
        <li class="contact__item">
          <svg class="contact__icon" viewBox="0 0 18 18"><path d="M2 6c0-3 3-4 7-4s7 1 7 4l-3 1-1-2H6L5 7zM4 9h10l2 7H2z"/></svg>
          0438615207
        </li>
        <li class="contact__item">
          <svg class="contact__icon" viewBox="0 0 18 18"><path d="M5 1h8a1 1 0 0 1 1 1v14a1 1 0 0 1-1 1H5a1 1 0 0 1-1-1V2a1 1 0 0 1 1-1zm1 2v10h6V3zm3 11a1 1 0 1 0 0 2 1 1 0 0 0 0-2z"/></svg>
          1800 614 372
        </li>
        <li class="contact__item">
          <svg class="contact__icon" viewBox="0 0 18 18"><path d="M1 4h16v11H1zm1.5 1.2L9 10l6.5-4.8V5h-13z"/></svg>
          darren@orla.properties
        </li>
        <li class="contact__item">
          <svg class="contact__icon" viewBox="0 0 18 18"><path fill-rule="evenodd" d="M9 1a8 8 0 1 0 0 16A8 8 0 0 0 9 1zm0 1.6a6.4 6.4 0 1 1 0 12.8A6.4 6.4 0 0 1 9 2.6zM2.5 8.3h13v1.4h-13zM8.3 2.5h1.4v13H8.3z"/></svg>
          www.orla.properties
        </li>
        <li class="contact__item">
          <svg class="contact__icon" viewBox="0 0 18 18"><path d="M9 1a6 6 0 0 0-6 6c0 4.5 6 10 6 10s6-5.5 6-10a6 6 0 0 0-6-6zm0 8.5A2.5 2.5 0 1 1 9 4.5a2.5 2.5 0 0 1 0 5z"/></svg>
          <span>PO BOX 73 Bentleigh,<br>VIC 3024</span>
        </li>
      </ul>
    </div>
  </section>

</main>
</body>
</html>
```